UI design for a mobile app that manages color schemes/pallettes

Should look cool, different, and modern.
The UI colors should not compete with pallette colors (as much as possible)
Features:
Currently looking for 3 pages/screens for the app: Browse through all palettes, view/edit a single palette, import
Features to include in the UI:
- View the list of color palettes (each list item includes a preview showing all colors in that color palette)
- View a particular color palette.
- Each displayed color should show:
- hex value
- rgb(255, 255, 255) value
- Name of pallete
- Button to copy the palette to a new pallette
- Sliders to change the properties (hue, saturation, value) or all colors in the palette at once
- Ability to add color
- Ability to remove color
- Switch background color that the pallete is displayed on: (black, mid gray, white, custom)
- A page that allows you to import palettes from a folder
Look and feel
Each slider illustrates characteristics of the customer's brand and the style your logo design should communicate.

```html
<!DOCTYPE html>
<html lang="en">
<head>
<meta charset="utf-8">
<title>Palette Manager – App Screens</title>
<link href="https://fonts.googleapis.com/css2?family=Poppins:wght@400;500;600;700&display=swap" rel="stylesheet">
<style>
:root{
  --bg:#FBF0E7;
  --screen:#FFFFFF;
  --ink:#1B1B1F;
  --muted:#8A8A90;
  --line:#ECECEF;
  --accent:#EC6A4C;
  --accent-2:#F86B45;
  --accent-soft:#F4B9A8;
  --navy:#0F3047;
  --red:#C63A32;
  --orange:#E88431;
  --yellow:#F4C05F;
  --cream:#E9E2BC;
}
*{box-sizing:border-box;margin:0;padding:0}
html,body{width:1200px;height:864px;overflow:hidden}
body{background:var(--bg);font-family:'Poppins',sans-serif;color:var(--ink);position:relative}

.screen-label{position:absolute;font-weight:600;font-size:15px;white-space:nowrap}
.screen-label .num{position:absolute;left:-16px;top:-20px;font-size:48px;font-weight:700;color:var(--accent);opacity:.14;line-height:1;z-index:-1}

.screen{position:absolute;width:237px;height:512px;background:var(--screen);border-radius:28px;overflow:hidden;box-shadow:0 6px 24px rgba(160,90,60,.12)}
.status{position:absolute;top:12px;left:20px;right:16px;display:flex;justify-content:space-between;align-items:center;font-size:9px;font-weight:500}
.status svg{display:block}
.home-bar{position:absolute;bottom:8px;left:50%;width:84px;height:3px;margin-left:-42px;background:var(--ink);border-radius:2px}
.abs{position:absolute}
.back{position:absolute;left:13px;top:34px}
.h-title{position:absolute;left:0;right:0;top:33px;text-align:center;font-size:10px;font-weight:500}

/* screen 1 */
.page-title{position:absolute;left:13px;top:32px;font-size:12px;font-weight:600}
.import-link{position:absolute;right:16px;top:33px;display:flex;gap:4px;align-items:center;color:var(--accent);font-size:10px;font-weight:500}
.palette-card{position:absolute;left:13px;width:210px;height:65px;background:#fff;border-radius:8px;box-shadow:0 2px 8px rgba(0,0,0,.07)}
.palette-card .name{position:absolute;left:9px;top:8px;font-size:8px}
.palette-card .fav{position:absolute;right:9px;top:7px}
.palette-card .strip{position:absolute;left:7px;right:6px;top:28px;height:31px;display:flex;gap:3px}
.strip span{flex:1;border-radius:3px}
.tab-bar{position:absolute;left:0;right:0;top:456px;display:flex;justify-content:space-around;padding:0 14px}
.tab{display:flex;flex-direction:column;align-items:center;gap:3px;font-size:6px;color:var(--muted);width:50px}
.tab.active{color:var(--accent)}

/* screen 2 */
.icon-btn{position:absolute;top:30px;width:24px;height:24px;border-radius:50%;background:#fff;box-shadow:0 2px 6px rgba(0,0,0,.1);display:flex;align-items:center;justify-content:center}
.palette-title{position:absolute;left:13px;top:62px;font-size:12px;font-weight:600}
.color-row{position:absolute;left:13px;width:210px;height:47px;border-radius:8px;color:#fff;padding:9px 10px}
.color-row .hex{font-size:10px;font-weight:500}
.color-row .rgb{font-size:7.5px;margin-top:3px;word-spacing:6px}
.color-row .copy{position:absolute;right:9px;top:11px;width:25px;height:25px;border-radius:50%;background:rgba(0,0,0,.22);display:flex;align-items:center;justify-content:center}
.add-row{position:absolute;left:13px;top:352px;width:210px;height:32px;border-radius:6px;box-shadow:0 2px 8px rgba(236,106,76,.15);display:flex;align-items:center;justify-content:space-between;padding:0 11px 0 13px;color:var(--accent);font-size:8px;font-weight:600}
.sheet{position:absolute;left:0;right:0;top:453px;bottom:0;border-radius:14px 14px 0 0;box-shadow:0 -3px 10px rgba(0,0,0,.06);text-align:center;color:var(--accent);font-size:8px;font-weight:600;padding-top:6px}

/* screen 3/4 shared */
.swatch-row{position:absolute;left:13px;width:210px;height:39px;display:flex;gap:4px}
.swatch-row span{flex:1;border-radius:5px;display:flex;align-items:center;justify-content:center}
.swatch-row span.selected{box-shadow:0 0 0 2px #fff,0 2px 6px rgba(0,0,0,.25)}
.value-box{position:absolute;left:13px;width:210px;height:36px;border:1px solid var(--line);border-radius:6px}
.value-box .col{position:absolute;top:7px;text-align:center}
.value-box .lbl{font-size:5px;color:var(--muted);letter-spacing:.3px}
.value-box .val{font-size:9.5px;font-weight:600;margin-top:4px;word-spacing:4px}
.value-box .divider{position:absolute;left:82px;top:11px;width:1px;height:14px;background:var(--line)}
.value-box .copy-btn{position:absolute;right:6px;top:6px;width:25px;height:25px;border-radius:5px;background:linear-gradient(135deg,var(--accent),var(--accent-2));display:flex;align-items:center;justify-content:center}
.action-btn{position:absolute;width:99px;height:31px;border-radius:6px;box-shadow:0 2px 8px rgba(0,0,0,.07);display:flex;align-items:center;justify-content:space-between;padding:0 10px;color:var(--accent);font-size:8px;font-weight:600}
.section-title{position:absolute;left:13px;font-size:10px;font-weight:600}
.panel-edge{position:absolute;left:0;right:0;height:12px;border-radius:12px 12px 0 0;box-shadow:0 -3px 8px rgba(0,0,0,.05)}
.slider{position:absolute;left:13px;width:210px;height:25px}
.slider .axis{position:absolute;left:0;top:6px;font-size:8px;font-weight:500}
.slider .track{position:absolute;left:19px;right:0;top:0;height:25px;border-radius:13px}
.slider .knob{position:absolute;top:4px;width:24px;height:17px;border-radius:9px;background:#fff;font-size:6.5px;font-weight:600;display:flex;align-items:center;justify-content:center;box-shadow:0 1px 3px rgba(0,0,0,.2)}
.primary-btn{position:absolute;left:13px;width:210px;height:31px;border-radius:8px;background:linear-gradient(90deg,var(--accent),var(--accent-2));color:#fff;font-size:9px;font-weight:600;display:flex;align-items:center;justify-content:center;box-shadow:0 3px 8px rgba(236,106,76,.3)}
.image-slot{position:absolute;left:13px;top:63px;width:210px;height:125px;border-radius:8px;background:linear-gradient(160deg,#E6507A 0%,#B43DE0 35%,#7A2BD8 55%,#19B8E8 75%,#3C40D9 100%)}
.field-label{position:absolute;left:13px;top:397px;font-size:6px;letter-spacing:.3px}
.field{position:absolute;left:13px;top:411px;width:210px;height:31px;border-radius:5px;background:#F8F8F9;font-size:8px;color:var(--muted);padding:9px 9px}
</style>
</head>
<body>

<!-- Labels -->
<div class="screen-label" style="left:94px;top:124px"><span class="num">01</span>Browse All Palettes Screen</div>
<div class="screen-label" style="left:388px;top:594px"><span class="num">02</span>View Palette Screen v1</div>
<div class="screen-label" style="left:657px;top:124px"><span class="num">03</span>View / Edit Palette Screen v2</div>
<div class="screen-label" style="left:929px;top:594px"><span class="num">04</span>Import Image from Gallery</div>

<!-- Screen 1: Browse -->
<section class="screen" style="left:57px;top:167px">
  <div class="status"><span>9:41</span><svg width="40" height="8" viewBox="0 0 40 8"><rect x="0" y="5" width="2" height="3" fill="#1B1B1F"/><rect x="3" y="3.5" width="2" height="4.5" fill="#1B1B1F"/><rect x="6" y="2" width="2" height="6" fill="#1B1B1F"/><rect x="9" y="0" width="2" height="8" fill="#1B1B1F"/><path d="M15 3.5a6 6 0 0 1 8 0M16.5 5a3.5 3.5 0 0 1 5 0" stroke="#1B1B1F" stroke-width="1.2" fill="none"/><circle cx="19" cy="7" r="1" fill="#1B1B1F"/><rect x="26" y="1" width="12" height="6" rx="1.5" fill="#1B1B1F"/></svg></div>
  <div class="page-title">All Palettes</div>
  <div class="import-link"><svg width="15" height="12" viewBox="0 0 15 12"><path d="M4 10H3.5a3 3 0 0 1 0-6 4 4 0 0 1 7.6-.5A3 3 0 0 1 11.5 10H11M7.5 6v5.5M5.5 8l2-2 2 2" fill="none" stroke="#EC6A4C" stroke-width="1.1" stroke-linecap="round" stroke-linejoin="round"/></svg>Import</div>

  <div class="palette-card" style="top:70px"><span class="name">Sample Palette Name</span>
    <svg class="fav" width="12" height="11" viewBox="0 0 12 11"><path d="M6 10 1.5 5.6A2.7 2.7 0 0 1 6 2a2.7 2.7 0 0 1 4.5 3.6Z" fill="none" stroke="#1B1B1F" stroke-width="1.1"/></svg>
    <div class="strip"><span style="background:#0F3047"></span><span style="background:#C63A32"></span><span style="background:#E88431"></span><span style="background:#F4C05F"></span><span style="background:#E9E2BC"></span></div></div>
  <div class="palette-card" style="top:149px"><span class="name">Name of Palette 101</span>
    <svg class="fav" width="12" height="11" viewBox="0 0 12 11"><path d="M6 10 1.5 5.6A2.7 2.7 0 0 1 6 2a2.7 2.7 0 0 1 4.5 3.6Z" fill="#EC6A4C"/></svg>
    <div class="strip"><span style="background:#FCCBAE"></span><span style="background:#FDB19E"></span><span style="background:#E3949A"></span><span style="background:#B6838B"></span><span style="background:#A83F62"></span><span style="background:#624F5E"></span></div></div>
  <div class="palette-card" style="top:227px"><span class="name">No. 3 Sample Pallete Name</span>
    <svg class="fav" width="12" height="11" viewBox="0 0 12 11"><path d="M6 10 1.5 5.6A2.7 2.7 0 0 1 6 2a2.7 2.7 0 0 1 4.5 3.6Z" fill="none" stroke="#1B1B1F" stroke-width="1.1"/></svg>
    <div class="strip"><span style="background:#8ECAE6"></span><span style="background:#219EBC"></span><span style="background:#023047"></span><span style="background:#FFB703"></span><span style="background:#FB8500"></span></div></div>
  <div class="palette-card" style="top:306px"><span class="name">Palette Sample 4</span>
    <svg class="fav" width="12" height="11" viewBox="0 0 12 11"><path d="M6 10 1.5 5.6A2.7 2.7 0 0 1 6 2a2.7 2.7 0 0 1 4.5 3.6Z" fill="none" stroke="#1B1B1F" stroke-width="1.1"/></svg>
    <div class="strip"><span style="background:#CCD2C6"></span><span style="background:#8AA38B"></span><span style="background:#5A766C"></span><span style="background:#3A4D4F"></span><span style="background:#2F3B40"></span></div></div>
  <div class="palette-card" style="top:384px"><span class="name">No. 6 Palette Name</span>
    <svg class="fav" width="12" height="11" viewBox="0 0 12 11"><path d="M6 10 1.5 5.6A2.7 2.7 0 0 1 6 2a2.7 2.7 0 0 1 4.5 3.6Z" fill="none" stroke="#1B1B1F" stroke-width="1.1"/></svg>
    <div class="strip"><span style="background:#264653"></span><span style="background:#2A9D8F"></span><span style="background:#E9C46A"></span><span style="background:#F4A261"></span><span style="background:#E76F51"></span></div></div>

  <nav class="tab-bar">
    <div class="tab active"><svg width="15" height="15" viewBox="0 0 15 15"><rect x="1" y="0" width="13" height="1" fill="#EC6A4C"/><rect x="1" y="3" width="13" height="5" rx="1" fill="#EC6A4C"/><rect x="1" y="9" width="6" height="5" rx="1" fill="#EC6A4C"/><rect x="8" y="9" width="6" height="5" rx="1" fill="#EC6A4C"/></svg>Palettes</div>
    <div class="tab"><svg width="15" height="14" viewBox="0 0 15 14"><path d="M7.5 13 1.8 7.2A3.4 3.4 0 0 1 7.5 2.6a3.4 3.4 0 0 1 5.7 4.6Z" fill="none" stroke="#8A8A90" stroke-width="1.1"/></svg>Favourites</div>
    <div class="tab"><svg width="15" height="14" viewBox="0 0 15 14"><circle cx="3" cy="7" r="1.3" fill="#8A8A90"/><circle cx="7.5" cy="7" r="1.3" fill="#8A8A90"/><circle cx="12" cy="7" r="1.3" fill="#8A8A90"/></svg>More</div>
  </nav>
  <div class="home-bar"></div>
</section>

<!-- Screen 2: View palette v1 -->
<section class="screen" style="left:340px;top:54px">
  <div class="status"><span>9:41</span><svg width="40" height="8" viewBox="0 0 40 8"><rect x="0" y="5" width="2" height="3" fill="#1B1B1F"/><rect x="3" y="3.5" width="2" height="4.5" fill="#1B1B1F"/><rect x="6" y="2" width="2" height="6" fill="#1B1B1F"/><rect x="9" y="0" width="2" height="8" fill="#1B1B1F"/><path d="M15 3.5a6 6 0 0 1 8 0M16.5 5a3.5 3.5 0 0 1 5 0" stroke="#1B1B1F" stroke-width="1.2" fill="none"/><circle cx="19" cy="7" r="1" fill="#1B1B1F"/><rect x="26" y="1" width="12" height="6" rx="1.5" fill="#1B1B1F"/></svg></div>
  <svg class="back" width="12" height="10" viewBox="0 0 12 10"><path d="M11 5H1.5M5 1 1 5l4 4" fill="none" stroke="#EC6A4C" stroke-width="1.3" stroke-linecap="round" stroke-linejoin="round"/></svg>
  <div class="icon-btn" style="right:50px"><svg width="12" height="11" viewBox="0 0 12 11"><path d="M6 10 1.5 5.6A2.7 2.7 0 0 1 6 2a2.7 2.7 0 0 1 4.5 3.6Z" fill="#EC6A4C"/></svg></div>
  <div class="icon-btn" style="right:13px"><svg width="12" height="4" viewBox="0 0 12 4"><circle cx="2" cy="2" r="1.2" fill="#EC6A4C"/><circle cx="6" cy="2" r="1.2" fill="#EC6A4C"/><circle cx="10" cy="2" r="1.2" fill="#EC6A4C"/></svg></div>
  <div class="palette-title">Sample Palette Name</div>

  <div class="color-row" style="top:92px;background:var(--navy)"><div class="hex">#0F3047</div><div class="rgb">R:&nbsp;15 G:&nbsp;48 B:&nbsp;71</div><div class="copy"><svg width="12" height="12" viewBox="0 0 12 12"><rect x="1" y="1" width="7" height="7" rx="1.5" fill="none" stroke="#fff" stroke-width="1.1"/><rect x="4" y="4" width="7" height="7" rx="1.5" fill="none" stroke="#fff" stroke-width="1.1"/></svg></div></div>
  <div class="color-row" style="top:142px;background:var(--red)"><div class="hex">#C63A32</div><div class="rgb">R:&nbsp;198 G:&nbsp;50 B:&nbsp;50</div><div class="copy"><svg width="12" height="12" viewBox="0 0 12 12"><rect x="1" y="1" width="7" height="7" rx="1.5" fill="none" stroke="#fff" stroke-width="1.1"/><rect x="4" y="4" width="7" height="7" rx="1.5" fill="none" stroke="#fff" stroke-width="1.1"/></svg></div></div>
  <div class="color-row" style="top:192px;background:var(--orange)"><div class="hex">#E88431</div><div class="rgb">R:&nbsp;232 G:&nbsp;132 B:&nbsp;49</div><div class="copy"><svg width="12" height="12" viewBox="0 0 12 12"><rect x="1" y="1" width="7" height="7" rx="1.5" fill="none" stroke="#fff" stroke-width="1.1"/><rect x="4" y="4" width="7" height="7" rx="1.5" fill="none" stroke="#fff" stroke-width="1.1"/></svg></div></div>
  <div class="color-row" style="top:243px;background:var(--yellow)"><div class="hex">#F4C05F</div><div class="rgb">R:&nbsp;244 G:&nbsp;192 B:&nbsp;85</div><div class="copy"><svg width="12" height="12" viewBox="0 0 12 12"><rect x="1" y="1" width="7" height="7" rx="1.5" fill="none" stroke="#fff" stroke-width="1.1"/><rect x="4" y="4" width="7" height="7" rx="1.5" fill="none" stroke="#fff" stroke-width="1.1"/></svg></div></div>
  <div class="color-row" style="top:293px;background:var(--cream)"><div class="hex">#E9E2BC</div><div class="rgb">R:&nbsp;233 G:&nbsp;226 B:&nbsp;188</div><div class="copy"><svg width="12" height="12" viewBox="0 0 12 12"><rect x="1" y="1" width="7" height="7" rx="1.5" fill="none" stroke="#fff" stroke-width="1.1"/><rect x="4" y="4" width="7" height="7" rx="1.5" fill="none" stroke="#fff" stroke-width="1.1"/></svg></div></div>

  <div class="add-row">Add Color<svg width="12" height="12" viewBox="0 0 12 12"><circle cx="6" cy="6" r="5" fill="none" stroke="#EC6A4C" stroke-width="1.1"/><path d="M6 3.5v5M3.5 6h5" stroke="#EC6A4C" stroke-width="1.1" stroke-linecap="round"/></svg></div>
  <div class="sheet"><svg width="12" height="8" viewBox="0 0 12 8"><path d="M1 4 6 1l5 3M1 7l5-3 5 3" fill="none" stroke="#C4C4C8" stroke-width="1.1" stroke-linecap="round"/></svg><div style="margin-top:8px">Change Properties</div></div>
  <div class="home-bar"></div>
</section>

<!-- Screen 3: View / edit v2 -->
<section class="screen" style="left:623px;top:167px">
  <div class="status"><span>9:41</span><svg width="40" height="8" viewBox="0 0 40 8"><rect x="0" y="5" width="2" height="3" fill="#1B1B1F"/><rect x="3" y="3.5" width="2" height="4.5" fill="#1B1B1F"/><rect x="6" y="2" width="2" height="6" fill="#1B1B1F"/><rect x="9" y="0" width="2" height="8" fill="#1B1B1F"/><path d="M15 3.5a6 6 0 0 1 8 0M16.5 5a3.5 3.5 0 0 1 5 0" stroke="#1B1B1F" stroke-width="1.2" fill="none"/><circle cx="19" cy="7" r="1" fill="#1B1B1F"/><rect x="26" y="1" width="12" height="6" rx="1.5" fill="#1B1B1F"/></svg></div>
  <svg class="back" width="12" height="10" viewBox="0 0 12 10" style="top:37px"><path d="M11 5H1.5M5 1 1 5l4 4" fill="none" stroke="#EC6A4C" stroke-width="1.3" stroke-linecap="round" stroke-linejoin="round"/></svg>
  <div class="h-title" style="top:34px">Sample Palette Name</div>
  <svg class="abs" style="right:17px;top:36px" width="3" height="12" viewBox="0 0 3 12"><circle cx="1.5" cy="1.5" r="1.2" fill="#EC6A4C"/><circle cx="1.5" cy="6" r="1.2" fill="#EC6A4C"/><circle cx="1.5" cy="10.5" r="1.2" fill="#EC6A4C"/></svg>

  <div class="swatch-row" style="top:68px">
    <span class="selected" style="background:var(--navy)"><svg width="9" height="7" viewBox="0 0 9 7"><path d="M1 3.5 3.5 6 8 1" fill="none" stroke="#fff" stroke-width="1.3" stroke-linecap="round"/></svg></span>
    <span style="background:var(--red)"></span><span style="background:var(--orange)"></span><span style="background:var(--yellow)"></span><span style="background:var(--cream)"></span>
  </div>
  <div class="value-box" style="top:120px">
    <div class="col" style="left:18px;width:44px"><div class="lbl">HEX VALUE</div><div class="val">#0F3047</div></div>
    <div class="divider"></div>
    <div class="col" style="left:96px;width:64px"><div class="lbl">RGB VALUE</div><div class="val">15 48 71</div></div>
    <div class="copy-btn"><svg width="12" height="12" viewBox="0 0 12 12"><rect x="1" y="1" width="7" height="7" rx="1.5" fill="none" stroke="#fff" stroke-width="1.1"/><rect x="4" y="4" width="7" height="7" rx="1.5" fill="#EC6A4C" stroke="#fff" stroke-width="1.1"/></svg></div>
  </div>
  <div class="action-btn" style="left:13px;top:170px">Remove Color<svg width="10" height="12" viewBox="0 0 10 12"><path d="M1 3h8M3.5 3V1.5h3V3M2 3l.6 8h4.8L8 3M4 5v4M6 5v4" fill="none" stroke="#EC6A4C" stroke-width="1" stroke-linecap="round"/></svg></div>
  <div class="action-btn" style="left:124px;top:170px">Add Color<svg width="11" height="11" viewBox="0 0 11 11"><rect x="1" y="1" width="9" height="9" rx="1.5" fill="none" stroke="#EC6A4C" stroke-width="1"/><path d="M5.5 3.5v4M3.5 5.5h4" stroke="#EC6A4C" stroke-width="1" stroke-linecap="round"/></svg></div>

  <div class="panel-edge" style="top:214px"></div>
  <div class="section-title" style="top:228px">Adjust Properties</div>
  <div class="slider" style="top:255px"><span class="axis">R</span><div class="track" style="background:linear-gradient(90deg,#1a0000,#F20A0A)"><span class="knob" style="left:10px">15</span></div></div>
  <div class="slider" style="top:287px"><span class="axis">G</span><div class="track" style="background:linear-gradient(90deg,#001100,#08D40B)"><span class="knob" style="left:22px">48</span></div></div>
  <div class="slider" style="top:318px"><span class="axis">B</span><div class="track" style="background:linear-gradient(90deg,#140010,#0337D6)"><span class="knob" style="left:56px">71</span></div></div>
  <div class="slider" style="top:362px"><span class="axis">H</span><div class="track" style="background:linear-gradient(90deg,#F20A2A,#F7E600 22%,#0BD02A 42%,#00D0D8 55%,#2A3AF0 70%,#F000E0 85%,#F0104A)"><span class="knob" style="left:117px">242</span></div></div>
  <div class="slider" style="top:393px"><span class="axis">S</span><div class="track" style="background:linear-gradient(90deg,#FFFFFF,#3B7FF0)"><span class="knob" style="left:87px">126</span></div></div>

  <div class="primary-btn" style="top:458px">Save Pallete</div>
  <div class="home-bar"></div>
</section>

<!-- Screen 4: Import -->
<section class="screen" style="left:906px;top:54px">
  <div class="status"><span>9:41</span><svg width="40" height="8" viewBox="0 0 40 8"><rect x="0" y="5" width="2" height="3" fill="#1B1B1F"/><rect x="3" y="3.5" width="2" height="4.5" fill="#1B1B1F"/><rect x="6" y="2" width="2" height="6" fill="#1B1B1F"/><rect x="9" y="0" width="2" height="8" fill="#1B1B1F"/><path d="M15 3.5a6 6 0 0 1 8 0M16.5 5a3.5 3.5 0 0 1 5 0" stroke="#1B1B1F" stroke-width="1.2" fill="none"/><circle cx="19" cy="7" r="1" fill="#1B1B1F"/><rect x="26" y="1" width="12" height="6" rx="1.5" fill="#1B1B1F"/></svg></div>
  <svg class="back" width="12" height="10" viewBox="0 0 12 10" style="top:37px"><path d="M11 5H1.5M5 1 1 5l4 4" fill="none" stroke="#EC6A4C" stroke-width="1.3" stroke-linecap="round" stroke-linejoin="round"/></svg>
  <div class="h-title" style="top:34px">Import</div>
  <div class="image-slot" role="img" aria-label="Imported gallery image: abstract flowing waves in orange, magenta, purple and cyan"></div>
  <div class="action-btn" style="left:13px;top:200px;width:99px">Upload Photo<svg width="14" height="11" viewBox="0 0 14 11"><path d="M4 9.5H3.5a2.8 2.8 0 0 1 0-5.6 3.8 3.8 0 0 1 7.2-.5A2.8 2.8 0 0 1 10.5 9.5H10M7 5.5v5M5 7.5l2-2 2 2" fill="none" stroke="#EC6A4C" stroke-width="1" stroke-linecap="round" stroke-linejoin="round"/></svg></div>
  <div class="action-btn" style="left:124px;top:200px;width:99px">Take Photo<svg width="13" height="11" viewBox="0 0 13 11"><path d="M1 3.5h2.5l1-1.8h4l1 1.8H12v6.5H1Z" fill="none" stroke="#EC6A4C" stroke-width="1" stroke-linejoin="round"/><circle cx="6.5" cy="6.5" r="2" fill="none" stroke="#EC6A4C" stroke-width="1"/></svg></div>

  <div class="panel-edge" style="top:252px"></div>
  <div class="section-title" style="top:264px">Extracted Colors</div>
  <div class="swatch-row" style="top:292px">
    <span class="selected" style="background:#46BCD9"><svg width="9" height="7" viewBox="0 0 9 7"><path d="M1 3.5 3.5 6 8 1" fill="none" stroke="#fff" stroke-width="1.3" stroke-linecap="round"/></svg></span>
    <span style="background:#F0957A"></span><span style="background:#EE8848"></span><span style="background:#A03DD8"></span><span style="background:#2E3696"></span>
  </div>
  <div class="value-box" style="top:344px">
    <div class="col" style="left:14px;width:52px"><div class="lbl">HEX VALUE</div><div class="val">#46BCD9</div></div>
    <div class="divider"></div>
    <div class="col" style="left:92px;width:68px"><div class="lbl">RGB VALUE</div><div class="val">70 188 217</div></div>
    <div class="copy-btn"><svg width="12" height="12" viewBox="0 0 12 12"><rect x="1" y="1" width="7" height="7" rx="1.5" fill="none" stroke="#fff" stroke-width="1.1"/><rect x="4" y="4" width="7" height="7" rx="1.5" fill="#EC6A4C" stroke="#fff" stroke-width="1.1"/></svg></div>
  </div>
  <div class="field-label">PALETTE NAME</div>
  <div class="field">Enter Here</div>
  <div class="primary-btn" style="top:457px">Save to Favourites</div>
  <div class="home-bar"></div>
</section>

</body>
</html>
```